Flyer für den Bereich Solarenergie
Zielgruppe
Guten Tag,
wir sind im Bereich Solarenergie tätig. Wir suchen nun Hallen mit großen Dächern, die wir anmieten können, um darauf Solaranlagen zu bauen. Wir machen dabei alles aus einer Hand. der Eigentümer muss nichts machen. Er bekommt sogar Geld von uns und das Dach ist sowieso meistens leer.
Aufgabenstellung
Wir möchten einen DINA4 Flyer den wir als PDF in Emails verschicken können. Farbdaten sollten Sie aus den Logodateien im Anhang entnehmen können. Richten Sie sich auch gerne an das Design des Logos und der Website. Dabei sollen kurz die wichtigsten Key Faktoren aufgelistet werden und das Unternehmen kurz dargestellt werden. Hier einmal die Texte:
Beschreibung zum Unternehmen:
Veltrano ist Experte für grüne Energietechnik mit über 20 Jahren Erfahrung. Mit über 1.000 zufriedenen Kunden im Bereich Photovoltaikanlagen können wir auf einen großen Erfahrungsschatz zurückgreifen. Wenn wir am Werk sind, wird nicht nur das Klima geschont, sondern auch Sie als Kunde profitieren. Mit uns wird nachhaltiges Handeln kinderleicht und gleichzeitig rentabel.
Erwirtschaften auch Sie mit Ihrem Dach nun bares Geld!
Ihre Vorteile:
- Umwelt schonen durch das Produzieren von grünem Strom
- Dach schützen vor Emissionen
- Dachsanierungen anstatt von Mietzahlungen möglich
- Keine Kosten, da wir alle Kosten der Anträge, der Anlage und aller Arbeiten übernehmen
- Mieteinnahmen generieren!
Einzige Voraussetzung:
Dachfläche mit mind. 1.500qm
Worauf warten Sie?
Nehmen Sie jetzt Kontakt auf für eine entsprechende Machbarkeitsprüfung. Natürlich ist auch das Kostenlos.
veltrano GmbH
Fennstraße 47b
48155 Münster
T: +49 176 528 914 03
E: info@veltrano-beispiel.de

```html
<!DOCTYPE html>
<html lang="de">
<head>
<meta charset="utf-8">
<title>Veltrano – Solarflyer</title>
<link href="https://fonts.googleapis.com/css2?family=Montserrat:wght@800&family=Raleway:wght@400;500;700;800&display=swap" rel="stylesheet">
<style>
  :root {
    --sage: #dde4d8;
    --khaki: #d0cea6;
    --leaf-light: #c0d68e;
    --leaf: #a5bd3a;
    --icon-green: #93ab3a;
    --ink: #34363a;
    --olive: #55552c;
    --white: #ffffff;
  }
  * { margin: 0; padding: 0; box-sizing: border-box; }
  html, body { width: 848px; height: 1200px; overflow: hidden; background: var(--sage); }
  .flyer {
    position: relative; width: 848px; height: 1200px; overflow: hidden;
    background: var(--sage); font-family: "Raleway", sans-serif; color: var(--olive);
  }
  .backdrop { position: absolute; inset: 0; }
  .brand {
    position: absolute; left: 41px; top: 26px;
    font-family: "Raleway", sans-serif; font-weight: 500; font-size: 44px;
    color: var(--ink); letter-spacing: -0.5px;
  }
  .headline {
    position: absolute; left: 38px; top: 122px;
    font-family: "Montserrat", sans-serif; font-weight: 800; font-size: 63px;
    line-height: 82px; color: var(--ink); letter-spacing: -0.5px; text-transform: uppercase;
  }
  .benefits { position: absolute; left: 32px; top: 0; list-style: none; }
  .benefit { position: absolute; left: 0; width: 600px; }
  .benefit-icon { position: absolute; left: 0; top: 0; width: 68px; height: 68px; }
  .benefit-title { position: absolute; left: 86px; top: 0; font-weight: 700; font-size: 19px; white-space: nowrap; }
  .benefit-text { position: absolute; left: 86px; top: 27px; font-weight: 400; font-size: 19px; line-height: 24px; width: 440px; }
  .accent-bar { position: absolute; left: 41px; top: 1079px; width: 138px; height: 11px; background: var(--leaf); }
  .website { position: absolute; left: 41px; top: 1120px; font-weight: 800; font-size: 28px; color: var(--olive); }
  .cta {
    position: absolute; left: 430px; top: 968px; width: 340px; text-align: center;
    font-family: "Raleway", sans-serif; font-weight: 800; font-size: 21.5px; line-height: 28px;
    color: var(--white); text-transform: uppercase;
  }
  .contact { position: absolute; left: 413px; top: 1101px; list-style: none; color: var(--white); font-weight: 800; font-size: 19px; }
  .contact li { display: flex; align-items: center; gap: 10px; height: 24px; }
  .contact svg { width: 20px; height: 20px; }
</style>
</head>
<body>
<div class="flyer">
  <svg class="backdrop" width="848" height="1200" viewBox="0 0 848 1200">
    <polygon points="301,0 620,0 458,277" fill="var(--khaki)"/>
    <polygon points="690,0 848,0 848,272" fill="var(--khaki)"/>
    <polygon points="657,0 489,277 817,277" fill="var(--leaf-light)"/>
    <defs>
      <linearGradient id="panelTones" x1="0" y1="0" x2="1" y2="1">
        <stop offset="0" stop-color="#8fb0dc"/><stop offset="0.5" stop-color="#5a6f96"/><stop offset="1" stop-color="#2f4f9c"/>
      </linearGradient>
      <linearGradient id="roofTones" x1="0" y1="0" x2="0" y2="1">
        <stop offset="0" stop-color="#9cc0e6"/><stop offset="0.45" stop-color="#c35a34"/><stop offset="0.8" stop-color="#e9e6de"/><stop offset="1" stop-color="#6f8a3a"/>
      </linearGradient>
    </defs>
    <g role="img" aria-label="Foto: Monteur installiert Solarmodule auf einem Dach">
      <polygon points="489,309 815,309 652,594" fill="url(#panelTones)"/>
      <polygon points="666,594 831,309 848,309 848,594" fill="url(#panelTones)"/>
    </g>
    <g role="img" aria-label="Foto: Wohnhaus mit Solaranlage auf rotem Ziegeldach">
      <polygon points="653,629 489,913 817,913" fill="url(#roofTones)"/>
      <polygon points="684,628 848,628 848,913" fill="url(#roofTones)"/>
    </g>
    <polygon points="458,943 816,943 667,1200 311,1200" fill="var(--leaf)"/>
    <polygon points="848,944 848,1200 698,1200" fill="var(--khaki)"/>
  </svg>

  <div class="brand">veltrano</div>

  <h1 class="headline">Verdienen Sie bares<br>Geld mit Ihrem Dach!</h1>

  <ul class="benefits">
    <li class="benefit" style="top:331px">
      <svg class="benefit-icon" viewBox="0 0 68 68"><circle cx="34" cy="34" r="34" fill="var(--icon-green)"/><g fill="none" stroke="#fff" stroke-width="1.6" stroke-linecap="round"><path d="M16 44 q10 -6 20 -2 l10 -6"/><path d="M16 48 q12 2 28 -8"/><path d="M34 36 q-8 -10 0 -16 q6 8 0 16z"/><path d="M36 34 q8 -8 16 -6 q-4 8 -16 6z"/></g></svg>
      <span class="benefit-title">Umweltschutz</span>
      <p class="benefit-text">Umwelt schonen durch das<br>Produzieren von grünem Strom.</p>
    </li>
    <li class="benefit" style="top:460px">
      <svg class="benefit-icon" viewBox="0 0 68 68"><circle cx="34" cy="34" r="34" fill="var(--icon-green)"/><g fill="none" stroke="#fff" stroke-width="1.6"><circle cx="34" cy="28" r="12"/><path d="M22 28 h24 M34 16 v24"/><path d="M14 30 v12 l10 8 M54 30 v12 l-10 8"/></g></svg>
      <span class="benefit-title">Nachhaltig</span>
      <p class="benefit-text">Ihr Dach ist vor Emissionen geschützt.</p>
    </li>
    <li class="benefit" style="top:583px">
      <svg class="benefit-icon" viewBox="0 0 68 68"><circle cx="34" cy="34" r="34" fill="var(--icon-green)"/><g fill="none" stroke="#fff" stroke-width="1.6"><rect x="20" y="14" width="28" height="40" rx="2"/><path d="M28 22 h14 M28 29 h14 M28 36 h14 M28 43 h14"/><circle cx="24.5" cy="22" r="1.6"/><circle cx="24.5" cy="29" r="1.6"/><circle cx="24.5" cy="36" r="1.6"/><circle cx="24.5" cy="43" r="1.6"/></g></svg>
      <span class="benefit-title">Planbar</span>
      <p class="benefit-text" style="width:520px">Dachsanierungen anstatt von Mietzahlungen möglich.</p>
    </li>
    <li class="benefit" style="top:706px">
      <svg class="benefit-icon" viewBox="0 0 68 68"><circle cx="34" cy="34" r="34" fill="var(--icon-green)"/><g fill="none" stroke="#fff" stroke-width="1.6"><rect x="18" y="26" width="26" height="26"/><path d="M16 26 h30 M31 26 v26"/><path d="M31 26 q-8 -10 -12 -4 q2 4 12 4 q8 -10 12 -4 q-2 4 -12 4"/><rect x="42" y="34" width="10" height="16" transform="rotate(-35 47 42)"/></g></svg>
      <span class="benefit-title">Kostenfrei</span>
      <p class="benefit-text">Wir übernehmen alle Kosten der Anträge, der Anlage und aller Arbeiten.</p>
    </li>
    <li class="benefit" style="top:829px">
      <svg class="benefit-icon" viewBox="0 0 68 68"><circle cx="34" cy="34" r="34" fill="var(--icon-green)"/><path d="M28 18 h12 l-3 6 q14 8 10 20 q-2 8 -13 8 q-11 0 -13 -8 q-4 -12 10 -20z" fill="#fff"/><text x="34" y="46" text-anchor="middle" font-family="Raleway, sans-serif" font-size="14" fill="var(--icon-green)">€</text></svg>
      <span class="benefit-title">Zuverdienst</span>
      <p class="benefit-text" style="width:520px">Sie generieren durch uns Mieteinnahmen.</p>
    </li>
    <li class="benefit" style="top:952px">
      <svg class="benefit-icon" viewBox="0 0 68 68"><circle cx="34" cy="34" r="34" fill="var(--icon-green)"/><g fill="none" stroke="#fff" stroke-width="1.6"><path d="M6 38 l28 -16 l28 16"/><path d="M12 38 l22 -12 l20 11"/></g></svg>
      <span class="benefit-title">Voraussetzung</span>
      <p class="benefit-text">Dachfläche mit mind. 1.500qm.</p>
    </li>
  </ul>

  <div class="accent-bar"></div>
  <div class="website">www.veltrano-beispiel.de</div>

  <p class="cta">Kontaktieren Sie uns<br>für eine kostenlose<br>Machbarkeitsprüfung!</p>

  <ul class="contact">
    <li><svg viewBox="0 0 20 20"><path d="M4 2 l4 0 l1 5 l-2 2 q2 4 5 5 l2 -2 l5 1 l0 4 q-1 2 -3 2 q-8 -1 -14 -10 q-1 -3 2 -7z" fill="#fff"/></svg>+49 176 528 914 03</li>
    <li><svg viewBox="0 0 20 20"><rect x="1" y="4" width="18" height="13" fill="#fff"/><path d="M1 4 l9 7 l9 -7" fill="none" stroke="var(--leaf)" stroke-width="1.6"/></svg>info@veltrano-beispiel.de</li>
  </ul>
</div>
</body>
</html>
```